Create a banner for a Gmail email signature

We need a graphic design to use in a solicitor's email signature. The banner will incorporate a head shot of the solicitor as well as the law firm's logo and contact details. The solicitor's photo and law firm's logo are uploaded in the task.

```html
<!DOCTYPE html>
<html lang="en">
<head>
<meta charset="utf-8">
<title>Email Signature – Marion</title>
<link rel="stylesheet" href="https://fonts.googleapis.com/css2?family=Montserrat:wght@400;500;700&display=swap">
<style>
  :root {
    --brand-plum: #8c1c5c;
    --ink: #222222;
    --rule-dark: #111111;
    --paper: #ffffff;
    --photo-light: #d9d4cf;
    --photo-mid: #b9aa95;
    --photo-dark: #5e5f66;
  }
  * { margin: 0; padding: 0; box-sizing: border-box; }
  html, body {
    width: 1200px;
    height: 541px;
    overflow: hidden;
    background: var(--paper);
  }
  .signature {
    position: relative;
    width: 1200px;
    height: 541px;
    font-family: "Montserrat", sans-serif;
    color: var(--ink);
    background: var(--paper);
  }
  .person-name {
    position: absolute;
    left: 30px;
    top: 51px;
    font-size: 34px;
    font-weight: 700;
    color: var(--brand-plum);
    line-height: 1;
  }
  .person-role {
    position: absolute;
    left: 30px;
    top: 100px;
    font-size: 41px;
    font-weight: 400;
    line-height: 1;
  }
  .firm-mark {
    position: absolute;
    right: 36px;
    top: 72px;
    display: flex;
    align-items: center;
    gap: 12px;
  }
  .firm-dot {
    width: 16px;
    height: 16px;
    border-radius: 50%;
    background: var(--brand-plum);
  }
  .firm-name {
    font-size: 42px;
    font-weight: 500;
    color: var(--brand-plum);
    letter-spacing: 0.5px;
    line-height: 1;
  }
  .rule-top {
    position: absolute;
    left: 30px;
    top: 175px;
    width: 1140px;
    height: 4px;
    background: var(--brand-plum);
  }
  .headshot {
    position: absolute;
    left: 30px;
    top: 228px;
    width: 233px;
    height: 233px;
    background: linear-gradient(135deg, var(--photo-light) 0%, var(--photo-mid) 50%, var(--photo-dark) 100%);
  }
  .contact-list {
    position: absolute;
    left: 297px;
    top: 218px;
    display: grid;
    grid-template-columns: 203px auto;
    align-items: center;
  }
  .contact-label {
    font-size: 39px;
    font-weight: 700;
    color: var(--brand-plum);
    line-height: 51px;
  }
  .contact-value {
    font-size: 34px;
    font-weight: 500;
    line-height: 51px;
    white-space: nowrap;
  }
  .social-links {
    display: flex;
    gap: 14px;
    align-items: center;
  }
  .social-links svg { display: block; }
  .rule-bottom {
    position: absolute;
    left: 30px;
    top: 507px;
    width: 1140px;
    height: 5px;
    background: var(--rule-dark);
  }
</style>
</head>
<body>
  <div class="signature">
    <div class="person-name">Marion</div>
    <div class="person-role">Job description</div>

    <div class="firm-mark">
      <span class="firm-dot"></span>
      <span class="firm-name">HARBOURSIDE LAW</span>
    </div>

    <div class="rule-top"></div>

    <div class="headshot" role="img" aria-label="Headshot of the solicitor"></div>

    <div class="contact-list">
      <span class="contact-label">Phone:</span>
      <span class="contact-value">+12 4810 2257 46</span>

      <span class="contact-label">Address:</span>
      <span class="contact-value">415 Harbour Lane, Bayview, Land 2260</span>

      <span class="contact-label">Email:</span>
      <span class="contact-value">office@sample.org</span>

      <span class="contact-label">Website:</span>
      <span class="contact-value">sample.org</span>

      <span class="contact-label">Socials:</span>
      <span class="social-links" aria-label="Social media links">
        <svg width="33" height="33" viewBox="0 0 33 33"><circle cx="16.5" cy="16.5" r="14" fill="none" stroke="#8c1c5c" stroke-width="2.5"/></svg>
        <svg width="33" height="33" viewBox="0 0 33 33"><circle cx="16.5" cy="16.5" r="14" fill="none" stroke="#8c1c5c" stroke-width="2.5"/></svg>
        <svg width="33" height="33" viewBox="0 0 33 33"><circle cx="16.5" cy="16.5" r="14" fill="none" stroke="#8c1c5c" stroke-width="2.5"/></svg>
        <svg width="33" height="33" viewBox="0 0 33 33"><circle cx="16.5" cy="16.5" r="14" fill="none" stroke="#8c1c5c" stroke-width="2.5"/></svg>
      </span>
    </div>

    <div class="rule-bottom"></div>
  </div>
</body>
</html>
```